Iconic Australian Wine Brand looking for a complete brand makeover

- Require a new label design for the Bright Meadow range of wines
- Complete brand makeover with refreshed packaging design
- Inspiration for consumers to see the brand in a new light
- The final design should communicate fun, energetic and modern packaging with the aim of engaging our core target market of 20 - 35 year old female wine drinkers, while re-engaging our loyal female demographic of 35+ year olds.

Target Market(s)

Engage a Core target market of 20-35 year old female wine drinkers / secondary target market: re-engage our loyal female demographic of 35+ year olds

Requirements
Must have
• Complete brand makeover in order to re-engage our loyal female drinkers, now in their mid to late 30's
Nice to have
• Play on words for the Brand name

```html
<!DOCTYPE html>
<html lang="en">
<head>
<meta charset="utf-8">
<title>Bright Meadow – Pinot Gris Label</title>
<link rel="stylesheet" href="https://fonts.googleapis.com/css2?family=Cormorant+Garamond:wght@400;500&family=Great+Vibes&display=swap">
<style>
  :root {
    --backdrop-light: #ffffff;
    --backdrop-edge: #e4e4e4;
    --gold-deep: #b3822a;
    --gold-mid: #d9ad4a;
    --gold-bright: #f6dc8a;
    --label-black: #1d1d1d;
    --label-charcoal: #4a4b4d;
    --figure-white: #f1f1f1;
    --figure-grey: #cfcfcf;
    --ink-white: #ffffff;
    --ribbon-ink: #2e2410;
  }
  html, body {
    margin: 0;
    padding: 0;
    width: 1200px;
    height: 1000px;
    overflow: hidden;
  }
  body {
    background: radial-gradient(ellipse at center, var(--backdrop-light) 45%, var(--backdrop-edge) 100%);
  }
  .label-stage {
    width: 1200px;
    height: 1000px;
    display: flex;
    align-items: center;
    justify-content: center;
  }
  .wine-label {
    width: 560px;
    height: 804px;
    display: block;
    filter: drop-shadow(0 10px 18px rgba(0, 0, 0, 0.18));
  }
  .brand-name {
    font-family: "Cormorant Garamond", "Times New Roman", serif;
    font-weight: 400;
    font-size: 38px;
    fill: var(--ink-white);
  }
  .variety-name {
    font-family: "Great Vibes", cursive;
    font-size: 25px;
    fill: var(--ribbon-ink);
  }
  .vintage-year {
    font-family: "Cormorant Garamond", "Times New Roman", serif;
    font-weight: 500;
    font-size: 27px;
    fill: var(--ink-white);
  }
</style>
</head>
<body>
<main class="label-stage">
  <svg class="wine-label" viewBox="0 0 390 560" xmlns="http://www.w3.org/2000/svg" aria-labelledby="label-title">
    <title id="label-title">Bright Meadow Field Day Pinot Gris 2016 label</title>
    <defs>
      <linearGradient id="gold-rim" x1="0" y1="0" x2="1" y2="1">
        <stop offset="0" stop-color="var(--gold-deep)"/>
        <stop offset="0.4" stop-color="var(--gold-bright)"/>
        <stop offset="0.7" stop-color="var(--gold-mid)"/>
        <stop offset="1" stop-color="var(--gold-deep)"/>
      </linearGradient>
      <radialGradient id="label-field" cx="0.5" cy="0.3" r="0.75">
        <stop offset="0" stop-color="var(--label-charcoal)"/>
        <stop offset="1" stop-color="var(--label-black)"/>
      </radialGradient>
      <linearGradient id="figure-tone" x1="0" y1="0" x2="1" y2="0">
        <stop offset="0" stop-color="var(--figure-white)"/>
        <stop offset="0.5" stop-color="var(--figure-grey)"/>
        <stop offset="1" stop-color="var(--figure-white)"/>
      </linearGradient>
      <linearGradient id="ribbon-gold" x1="0" y1="0" x2="1" y2="0">
        <stop offset="0" stop-color="var(--gold-deep)"/>
        <stop offset="0.45" stop-color="var(--gold-bright)"/>
        <stop offset="1" stop-color="var(--gold-mid)"/>
      </linearGradient>
      <path id="label-outline" d="M 80 0 H 310 Q 330 0 340 20 Q 350 55 380 65 Q 390 68 390 85 V 500 Q 390 560 330 560 H 60 Q 0 560 0 500 V 85 Q 0 68 10 65 Q 40 55 50 20 Q 60 0 80 0 Z"/>
      <path id="variety-path" d="M 60 428 Q 195 414 330 428"/>
    </defs>

    <g class="label-rim">
      <use href="#label-outline" fill="url(#gold-rim)"/>
    </g>
    <g class="label-field" transform="translate(195 280) scale(0.92 0.945) translate(-195 -280)">
      <use href="#label-outline" fill="url(#label-field)"/>
    </g>
    <g class="label-inner-line" transform="translate(195 280) scale(0.885 0.92) translate(-195 -280)">
      <use href="#label-outline" fill="none" stroke="var(--gold-mid)" stroke-width="1.1"/>
    </g>

    <rect class="figure-artwork" x="78" y="32" width="168" height="350" rx="30"
          fill="url(#figure-tone)" opacity="0.9"
          role="img" aria-label="Illustration of four tall stylised female silhouettes standing side by side"/>

    <text class="brand-name" text-anchor="middle">
      <tspan x="272" y="70">B</tspan>
      <tspan x="272" y="125">R</tspan>
      <tspan x="272" y="180">I</tspan>
      <tspan x="272" y="235">G</tspan>
      <tspan x="272" y="290">H</tspan>
      <tspan x="272" y="345">T</tspan>
      <tspan x="310" y="70">M</tspan>
      <tspan x="310" y="125">E</tspan>
      <tspan x="310" y="180">A</tspan>
      <tspan x="310" y="235">D</tspan>
      <tspan x="310" y="290">O</tspan>
      <tspan x="310" y="345">W</tspan>
    </text>

    <g class="variety-ribbon">
      <path class="ribbon-tail" d="M 28 396 L 62 398 L 62 440 L 28 444 L 42 420 Z" fill="var(--gold-deep)"/>
      <path class="ribbon-tail" d="M 362 396 L 328 398 L 328 440 L 362 444 L 348 420 Z" fill="var(--gold-deep)"/>
      <path class="ribbon-band" d="M 45 402 Q 195 386 345 402 V 442 Q 195 426 45 442 Z" fill="url(#ribbon-gold)"/>
      <text class="variety-name" text-anchor="middle">
        <textPath href="#variety-path" startOffset="50%">Field Day Pinot Gris</textPath>
      </text>
    </g>

    <text class="vintage-year" x="195" y="502" text-anchor="middle">2016</text>
  </svg>
</main>
</body>
</html>
```